business stationery

have a gorgeous logo that needs to be incorporated on stationery. Was hoping to do something on letterhead that was a paper that looked like "bark" from a tree or something that resembled the "woods." Soft paper with some very basic natural elements. Same thing for business cards. Think American lakeside cabin. Organic. Natural. Calm and welcoming but clear to read and understand. Wanted to use alot of black.

Target Market(s)

buyers of Conrad Bellweather home. Client that would have more than one home and in need of rare pieces and items to furnish an upmarket lakeside holiday cabin in the woods. Someone who treasures beautiful hand made items, organic foods and a real crackling fire but with money to burn in it!

Industry/Entity Type

Business

Requirements
Must have
• My logo
My business name
www.thornbydell.example
Natural almost raw effect paper
My ABN: 62 730 514 907 (to be placed in small writing at the bottom of card/letterhead)
Nice to have
• The website will consist of a cabin door that you "open" with a creak sound effect and then you go "inside" to look at the various rooms to start shopping. Want to bring that element of texture and warmth into the stationary also.
Should not have
• Anything modern or hard to read items

```html
<!DOCTYPE html>
<html lang="en">
<head>
<meta charset="utf-8">
<title>Thornby Dell — Stationery</title>
<link rel="stylesheet" href="https://fonts.googleapis.com/css2?family=Oswald:wght@400;500;600&display=swap">
<style>
  :root {
    --page-bg: #ffffff;
    --paper-light: #e8d9bd;
    --paper-mid: #d8bf98;
    --paper-edge: #c4a47a;
    --ink: #121212;
    --wine: #6b1014;
    --charcoal: #1a1a1a;
    --charcoal-soft: #3a3a3a;
    --card-border: #2a2420;
  }
  html, body {
    margin: 0;
    padding: 0;
    width: 960px;
    height: 1200px;
    overflow: hidden;
    background: var(--page-bg);
    font-family: "Oswald", "Arial Narrow", sans-serif;
  }
  .canvas {
    position: relative;
    width: 960px;
    height: 1200px;
  }
  .paper {
    background: radial-gradient(ellipse at 50% 50%, var(--paper-light) 0%, var(--paper-mid) 60%, var(--paper-edge) 100%);
  }

  /* Letterhead */
  .letterhead {
    position: absolute;
    left: 142px;
    top: 128px;
    width: 661px;
    height: 936px;
    overflow: hidden;
  }
  .letterhead__corners {
    position: absolute;
    inset: 0;
    width: 100%;
    height: 100%;
  }
  .brand {
    position: absolute;
    text-align: right;
    color: var(--ink);
  }
  .brand__name {
    display: block;
    font-weight: 600;
    text-transform: uppercase;
    letter-spacing: 1px;
    line-height: 1;
  }
  .brand__by {
    display: block;
    color: var(--wine);
    font-weight: 400;
    text-transform: uppercase;
    letter-spacing: 0.5px;
  }
  .letterhead .brand {
    right: 24px;
    top: 86px;
  }
  .letterhead .brand__name { font-size: 46px; }
  .letterhead .brand__by { font-size: 7px; margin-top: 3px; }

  .letterhead__footer {
    position: absolute;
    top: 882px;
    left: 190px;
    font-size: 14px;
    color: var(--ink);
    white-space: nowrap;
  }
  .letterhead__web { font-weight: 600; }
  .letterhead__abn {
    position: absolute;
    left: 200px;
    top: 1px;
    font-size: 12px;
    font-weight: 400;
  }

  /* Business card */
  .card {
    position: absolute;
    left: 617px;
    top: 630px;
    width: 280px;
    height: 160px;
    border: 1px solid var(--card-border);
    border-radius: 8px;
    box-sizing: border-box;
    overflow: hidden;
  }
  .card .brand {
    left: 0;
    right: 0;
    top: 54px;
    text-align: center;
  }
  .card .brand__name { font-size: 28px; }
  .card .brand__by {
    font-size: 4.5px;
    text-align: right;
    padding-right: 58px;
    margin-top: 2px;
  }
  .card__person {
    position: absolute;
    right: 20px;
    top: 112px;
    text-align: right;
    line-height: 1.3;
  }
  .card__name {
    display: block;
    font-size: 9.5px;
    color: var(--wine);
  }
  .card__web {
    display: block;
    font-size: 7.5px;
    color: var(--ink);
  }
  .card__abn {
    position: absolute;
    left: 20px;
    top: 132px;
    font-size: 4.5px;
    color: var(--ink);
  }
</style>
</head>
<body>
<main class="canvas">

  <section class="letterhead paper" aria-label="Letterhead">
    <svg class="letterhead__corners" viewBox="0 0 661 936" preserveAspectRatio="none" aria-hidden="true">
      <defs>
        <linearGradient id="charcoal-fill" x1="0" y1="0" x2="1" y2="1">
          <stop offset="0" stop-color="var(--charcoal-soft)"/>
          <stop offset="1" stop-color="var(--charcoal)"/>
        </linearGradient>
      </defs>
      <!-- top-left corner -->
      <path d="M0 0 H158 C92 38 32 88 0 138 Z" fill="url(#charcoal-fill)"/>
      <path d="M172 0 H194 C112 52 48 128 30 220 C18 282 8 346 0 408 V158 C36 100 96 44 172 0 Z" fill="var(--wine)"/>
      <!-- bottom-right corner -->
      <path d="M661 936 H506 C568 900 626 850 661 800 Z" fill="url(#charcoal-fill)"/>
      <path d="M467 936 H490 C566 894 622 836 640 760 C650 720 656 690 661 664 V780 C630 840 556 900 467 936 Z" fill="var(--wine)"/>
    </svg>

    <div class="brand">
      <span class="brand__name">Thornby Dell</span>
      <span class="brand__by">By Wren Halloway</span>
    </div>

    <footer class="letterhead__footer">
      <span class="letterhead__web">www.thornbydell.example</span>
      <span class="letterhead__abn">ABN: 62 730 514 907</span>
    </footer>
  </section>

  <section class="card paper" aria-label="Business card">
    <div class="brand">
      <span class="brand__name">Thornby Dell</span>
      <span class="brand__by">By Wren Halloway</span>
    </div>
    <div class="card__person">
      <span class="card__name">Wren Halloway</span>
      <span class="card__web">www.thornbydell.example</span>
    </div>
    <span class="card__abn">ABN: 62 730 514 907</span>
  </section>

</main>
</body>
</html>
```